Stationary for Keeping Steady

we are in the process of creating a more professional image for our company Keeping Steady Paramedical Services. We have recently had a new logo and general brochure designed using artpitchhub and have been impressed by the quality of submissions.

We need:
- Letterhead (A4)
- Business Cards
- With compliments slips
- Email stationary

Letterhead information:
Address - 47 Wattlebrook Drive, Fernhollow Vic 3091
Phone - 1800 462 817
email - enquiries@keepsteady.com.au
Internet - www.keepsteady.com.au
ABN - 82 463 915 207
ACN - 264 871 035

Files need to be able to be edited in Illustrator CS2

Business Cards / with compliments slips / email stationary:
Double sided.
One side to have Name, Mobile number, company phone 1800462817, email, internet address

Files need to be able to be edited in Illustrator CS2 (except email stationary)

Our website is www.keepsteady.com.au for more information. Do not base designs on the website as it will eventually be revised.

Target Market(s)

Australian based businesses, government departments and schools. We specialise in corporate customers rather than public first aid course

Industry/Entity Type

Internet

Requirements
Must have
• Where applicable file to be editable in illustrator CS2 to allow future alterations.

```html
<!DOCTYPE html>
<html lang="en">
<head>
<meta charset="utf-8">
<title>Keeping Steady – With Compliments Slip</title>
<link rel="stylesheet" href="https://fonts.googleapis.com/css2?family=PT+Sans+Narrow:wght@700&family=Open+Sans:wght@400;700&display=swap">
<style>
  :root {
    --brand-red: #d8202a;
    --brand-red-deep: #b5141d;
    --brand-red-light: #e8454c;
    --paper: #ffffff;
    --ink-light: #ffffff;
  }
  html, body {
    margin: 0;
    padding: 0;
    overflow: hidden;
    background: var(--paper);
  }
  .slip {
    position: relative;
    width: 1200px;
    height: 543px;
    overflow: hidden;
    background: var(--paper);
    font-family: "Open Sans", Arial, sans-serif;
  }
  .slip__swoosh {
    position: absolute;
    inset: 0;
    width: 1200px;
    height: 543px;
  }
  .brand {
    position: absolute;
    left: 58px;
    top: 62px;
    display: flex;
    align-items: center;
    gap: 28px;
  }
  .brand__square {
    width: 130px;
    height: 130px;
    background: var(--brand-red);
  }
  .brand__name {
    margin: 0;
    color: var(--brand-red);
    font-family: "Open Sans", Arial, sans-serif;
    font-weight: 700;
    line-height: 1.1;
  }
  .brand__name-main {
    display: block;
    font-size: 60px;
    letter-spacing: -0.5px;
  }
  .brand__name-sub {
    display: block;
    font-size: 33px;
    margin-top: 6px;
  }
  .contact {
    position: absolute;
    left: 20px;
    top: 436px;
    color: var(--ink-light);
    font-size: 20px;
    line-height: 27px;
    letter-spacing: 0.2px;
  }
  .contact p { margin: 0; }
  .contact__web { margin-left: 58px; }
  .greeting {
    position: absolute;
    left: 688px;
    top: 394px;
    margin: 0;
    color: var(--brand-red);
    font-family: "PT Sans Narrow", "Arial Narrow", sans-serif;
    font-weight: 700;
    font-size: 38px;
    letter-spacing: 0.3px;
  }
</style>
</head>
<body>
  <div class="slip">
    <svg class="slip__swoosh" viewBox="0 0 1200 543" aria-hidden="true">
      <defs>
        <linearGradient id="topBand" x1="0" y1="0" x2="1" y2="1">
          <stop offset="0" stop-color="var(--brand-red-deep)"/>
          <stop offset="0.55" stop-color="var(--brand-red)"/>
          <stop offset="1" stop-color="var(--brand-red-light)"/>
        </linearGradient>
        <linearGradient id="bottomBand" x1="0" y1="0" x2="1" y2="0">
          <stop offset="0" stop-color="var(--brand-red)"/>
          <stop offset="1" stop-color="var(--brand-red-light)"/>
        </linearGradient>
      </defs>
      <path d="M250,0 C600,30 1000,140 1200,430 L1200,0 Z" fill="url(#topBand)"/>
      <path d="M0,325 C320,350 680,450 930,543 L0,543 Z" fill="url(#bottomBand)"/>
    </svg>

    <div class="brand">
      <div class="brand__square"></div>
      <h1 class="brand__name">
        <span class="brand__name-main">Keeping Steady</span>
        <span class="brand__name-sub">Paramedical Services Pty Ltd</span>
      </h1>
    </div>

    <p class="greeting">With Compliments</p>

    <div class="contact">
      <p>47 Wattlebrook Drive, Fernhollow Vic 3091</p>
      <p>1800 462 817</p>
      <p>enquiries@keepsteady.com.au<span class="contact__web">www.keepsteady.com.au</span></p>
    </div>
  </div>
</body>
</html>
```